Create a new website for "The Arcade at Fernbrook"

I need a website for a shopping center in Atlanta USA. I want a classy high end look with high end motion videos (which I will provide).
The purpose of website is to attract new tenants to fill up vacant office spaces we have.
we will highlight existing cool stores and advertise that this is a cool place to start a new tenants business or office . ideally IT businesses in Alpharetta city in Georgia state in USA

Target Market(s)

commercial office tenants

Industry/Entity Type

Real Estate

Contact Information for Business Card

classy high end design
Arcade at Fernbrook
address:
2870 Briarwell Pkwy
Alpharetta GA 30005

Logo Text

I am open. Anything that attracts new IT tech tenants to lease up shopping center/ office space

Coding

Coded - Design and coding required

Number of Pages Required

5+ page

Requirements
Must have
• easy to browse

here is a link to some photos. i will provide videos shortly

http://www.tomsereph.com/2014/04/Building-Photos-3/n-5N2dg/
Nice to have
• please look at some of mall websites i like. Moving videos and images on home page

I really like this one: https://www.plazaatcresthollow.com/

others are

https://lindorecenter.com/

https://www.discoverbrisket.com/

```html
<!DOCTYPE html>
<html lang="en">
<head>
<meta charset="utf-8">
<title>Fernbrook — Shopping &amp; Office Center</title>
<link href="https://fonts.googleapis.com/css2?family=Montserrat:wght@400;500;600;700&family=Raleway:wght@400;500;600&display=swap" rel="stylesheet">
<style>
:root{
  --navy:#14306b;
  --navy-dark:#0f2454;
  --navy-deep:#1a2b5a;
  --orange:#f7820e;
  --white:#ffffff;
  --ink:#1d1d1f;
  --muted:#6f7380;
  --light:#f4f5f8;
  --line:#e2e5ec;
}
*{box-sizing:border-box;margin:0;padding:0}
html,body{width:1200px;height:5172px;overflow:hidden}
body{font-family:"Raleway",sans-serif;color:var(--ink);background:var(--white)}
section,header{position:relative;width:1200px;overflow:hidden}
.abs{position:absolute}
.ph{position:absolute;display:block}
.eyebrow{font-family:"Montserrat",sans-serif;font-size:15px;font-weight:500;color:var(--orange);text-transform:uppercase;letter-spacing:.5px}
.h2{font-family:"Montserrat",sans-serif;font-weight:500;font-size:31px;line-height:38px}
.body{font-size:12.5px;line-height:22px;color:var(--muted)}
.btn{display:inline-block;background:var(--orange);color:#fff;border-radius:20px;font-family:"Montserrat",sans-serif;font-size:13px;padding:10px 28px}

/* top bar */
.topbar{height:40px;background:var(--navy-deep);color:#fff;font-size:12px;font-family:"Montserrat",sans-serif}
.topbar .contact{left:16px;top:12px}
.topbar .note{left:415px;top:11px;font-size:14px;font-weight:500}
.topbar .social{right:14px;top:14px;display:flex;gap:14px}
.topbar .social span{width:10px;height:10px;border-radius:50%;background:#fff;display:block}

/* hero */
.hero{height:678px;background:linear-gradient(180deg,#4a6ca8 0%,#3d5f9c 55%,#2c4a86 100%)}
.nav{right:42px;top:48px;display:flex;gap:38px;font-family:"Montserrat",sans-serif;font-size:16px;letter-spacing:3px;color:#fff;font-weight:500}
.hero .title{width:100%;text-align:center;top:258px;font-family:"Montserrat",sans-serif;font-weight:400;font-size:86px;letter-spacing:14px;color:#fff}
.hero .sub{width:100%;text-align:center;top:358px;font-family:"Montserrat",sans-serif;font-size:23px;letter-spacing:5px;color:#fff}

/* features */
.features{height:410px;display:flex}
.features>div{width:300px;height:410px;position:relative}
.feature-card{background:var(--navy);color:#fff;text-align:center;padding-top:62px}
.feature-card h3{font-family:"Montserrat",sans-serif;font-weight:400;font-size:20px;margin-top:18px}
.feature-card .rule{width:30px;height:2px;background:var(--orange);margin:9px auto 14px}
.feature-card p{font-size:12.5px;line-height:23px;padding:0 26px}
.feature-card .btn{margin-top:18px}

/* about */
.about{height:748px}
.about .frame{left:160px;top:104px;width:418px;height:520px;border:8px solid var(--orange)}
.about .copy{left:644px;top:174px;width:520px}
.about .h2{margin-top:26px}
.about .intro{margin-top:24px}
.about .points{display:flex;gap:40px;margin-top:22px}
.about .point{display:flex;gap:14px;width:220px}
.icon-circle{width:42px;height:42px;border-radius:50%;background:var(--orange);flex:none;display:flex;align-items:center;justify-content:center}
.about .point h4{font-family:"Montserrat",sans-serif;font-size:14px;font-weight:600}
.about .point p{font-size:12.5px;line-height:22px;color:var(--muted);margin-top:6px}
.about .outro{margin-top:20px}
.about .more{margin-top:14px;color:var(--orange);font-size:13px;font-weight:600}

/* locations */
.locations{height:834px;background:var(--navy)}
.locations .copy{left:572px;top:70px;width:600px;color:#fff}
.locations .h2{margin-top:20px;line-height:38px}
.locations .body{color:#dfe5f3;margin-top:20px}
.loc-card{top:291px;width:303px;height:347px;background:#fff}
.loc-card .txt{padding:18px 18px}
.loc-card h4{color:var(--orange);font-weight:500;font-size:14px}
.loc-card p{font-size:12px;color:var(--muted);margin-top:16px}
.loc-card .btn{margin-top:18px;padding:10px 28px}
.dots{display:flex;gap:10px;align-items:center}
.dots span{width:10px;height:10px;border-radius:50%;background:#8b96b8}
.dots .on{width:30px;border-radius:5px;background:var(--orange)}

/* listings */
.listings{height:854px;background:#fff;text-align:center}
.listings .eyebrow{position:absolute;width:100%;top:96px}
.listings .bar{left:586px;top:124px;width:28px;height:2px;background:var(--orange)}
.listings .h2{position:absolute;width:100%;top:140px;font-size:30px}
.listings .body{position:absolute;width:100%;top:184px}
.tile{color:#fff;font-family:"Montserrat",sans-serif;text-align:center;box-shadow:0 6px 18px rgba(0,0,0,.15)}
.tile .inner{position:absolute;left:0;right:0;top:50%;transform:translateY(-50%)}
.tile h5{font-size:13px;font-weight:500;letter-spacing:.5px}
.tile p{font-family:"Raleway",sans-serif;font-size:12px;margin:14px 0}
.tile .tag{display:inline-block;border:2px solid #fff;padding:9px 16px;font-size:11px}

/* why */
.why{height:682px;background:var(--navy)}
.why .copy{left:564px;top:90px;width:600px;color:#fff}
.why .h2{margin-top:18px}
.why .body{color:#dfe5f3;margin-top:20px}
.benefit{display:flex;gap:18px;width:270px;color:#fff}
.benefit .icon-circle{width:42px;height:42px}
.benefit .icon-circle.soft{background:#2b4c8f}
.benefit h4{font-family:"Montserrat",sans-serif;font-size:15px;font-weight:500}
.benefit p{font-size:12.5px;line-height:22px;color:#dfe5f3;margin-top:8px}

/* cta */
.cta{height:250px;background:linear-gradient(100deg,#aab6f0 0%,#7388d6 45%,#3b56a6 100%);color:#fff;text-align:center}
.cta p{position:absolute;width:100%;top:110px;font-size:20px;font-family:"Montserrat",sans-serif}
.cta b{text-decoration:underline;font-weight:700}

/* contact */
.contact-sec{height:676px;background:linear-gradient(180deg,#263f80 0%,#1f3673 100%);color:#fff;text-align:center}
.contact-sec .eyebrow{position:absolute;width:100%;top:100px}
.contact-sec .h2{position:absolute;width:100%;top:140px;font-size:30px}
.contact-sec .body{position:absolute;width:100%;top:194px;color:#dfe5f3}
.cbox{top:394px;width:154px;height:120px;border:1px solid rgba(255,255,255,.8);display:flex;flex-direction:column;align-items:center;justify-content:center;gap:10px;font-family:"Montserrat",sans-serif;font-size:14px;font-weight:500}
.quote{left:614px;top:470px;width:308px;height:142px;background:#fff;color:#333;text-align:left;padding:18px 28px;font-size:12px;line-height:22px}
.quote .qd{display:flex;gap:22px;margin-top:6px}
.quote .qd span{width:8px;height:8px;border-radius:50%;border:1px solid #14306b}
.quote .qd .on{background:#14306b}
</style>
</head>
<body>

<header class="topbar">
  <div class="abs contact">&#9990; (+347) 555 018 2290 &nbsp; &#9993; info@fernbrookarcade.com</div>
  <div class="abs note">contact us for more information</div>
  <div class="abs social"><span></span><span></span><span></span><span></span></div>
</header>

<section class="hero">
  <div class="ph" role="img" aria-label="White shopping and office building with a square tower under a blue sky, tinted navy" style="inset:0;background:linear-gradient(180deg,rgba(90,120,180,.6),rgba(30,60,120,.6))"></div>
  <nav class="abs nav"><span>SHOPS</span><span>OFFICE</span><span>ARTS</span><span>HAPPENINGS</span><span>VISIT</span></nav>
  <h1 class="abs title">FERNBROOK</h1>
  <div class="abs sub">SHOPPING &amp; OFFICE CENTER</div>
</section>

<section class="features">
  <div><span class="ph" role="img" aria-label="Building with steeple roof and trees and parked cars" style="inset:0;background:linear-gradient(160deg,#a9c3e6 0%,#d9d2c0 45%,#6f7d63 100%)"></span></div>
  <div class="feature-card">
    <svg width="34" height="52" viewBox="0 0 34 52" fill="none" stroke="#fff" stroke-width="2"><path d="M17 3c7 7 9 16 7 30H10C8 19 10 10 17 3z"/><circle cx="17" cy="19" r="4"/><path d="M10 27l-6 8v5l7-5M24 27l6 8v5l-7-5M13 38l4 10 4-10"/></svg>
    <h3>Our Mission</h3><div class="rule"></div>
    <p>Lorem ipsum dolor sit amet, consectetur adipiscing elit, sed do eiusmod tempor incididunt ut labore et.</p>
    <span class="btn">Learn more</span>
  </div>
  <div><span class="ph" role="img" aria-label="White tower of the shopping center with storefronts" style="inset:0;background:linear-gradient(180deg,#ffffff 0%,#e6ebf2 45%,#8c96a8 100%)"></span></div>
  <div class="feature-card">
    <svg width="60" height="56" viewBox="0 0 60 56" fill="none" stroke="#fff" stroke-width="2"><path d="M40 4l16 2-2 16-22 22-14-14z"/><circle cx="42" cy="18" r="4"/><path d="M18 30l-10 4 8 6M32 44l-4 10-6-8M10 50l10-10"/></svg>
    <h3>Our History</h3><div class="rule"></div>
    <p>Lorem ipsum dolor sit amet, consectetur adipiscing elit, sed do eiusmod tempor incididunt ut labore et.</p>
    <span class="btn">Learn more</span>
  </div>
</section>

<section class="about">
  <div class="abs frame"></div>
  <span class="ph" role="img" aria-label="Person working on a laptop at a wooden desk, seen from above" style="left:180px;top:128px;width:420px;height:512px;background:linear-gradient(135deg,#5d5448 0%,#8a7a62 50%,#2f3d5f 100%)"></span>
  <span class="ph" role="img" aria-label="Hands with notebook, coffee cup and tablet on a table" style="left:0;top:156px;width:434px;height:200px;background:linear-gradient(135deg,#3a2c22 0%,#9c7a5c 55%,#d8cdbf 100%)"></span>
  <span class="ph" role="img" aria-label="Coffee shop sign with warm lights" style="left:0;top:378px;width:490px;height:200px;background:linear-gradient(135deg,#2a1a12 0%,#7a4a2a 50%,#3d5770 100%)"></span>
  <div class="abs copy">
    <div class="eyebrow">About Us</div>
    <h2 class="h2">Professional, Creative,<br>Flexible, Scalable Workspace</h2>
    <p class="body intro">Lorem Ipsum is simply dummy text of the printing and typesetting industry. Lorem Ipsum has been the industry's standard dummy text.</p>
    <div class="points">
      <div class="point"><span class="icon-circle"><svg width="18" height="18" viewBox="0 0 18 18" fill="#fff"><rect x="3" y="2" width="12" height="15"/></svg></span><div><h4>Workspace</h4><p>Lorem ipsum dolor sit amet, consectetur adipiscing elit.</p></div></div>
      <div class="point"><span class="icon-circle"><svg width="18" height="18" viewBox="0 0 18 18" fill="#fff"><rect x="2" y="6" width="6" height="11"/><rect x="10" y="2" width="6" height="15"/></svg></span><div><h4>Global network</h4><p>Lorem ipsum dolor sit amet, consectetur adipiscing elit.</p></div></div>
    </div>
    <p class="body outro">Lorem ipsum dolor sit amet, consectetur adipiscing elit, sed do eiusmod tempor incididunt ut labore et dolore magna aliqua. Quis ipsum suspendisse ultrices gravida.</p>
    <div class="more">More About Us&#10230;</div>
  </div>
</section>

<section class="locations">
  <span class="ph" role="img" aria-label="Street map of New York City and surrounding area with location markers" style="left:0;top:0;width:500px;height:834px;background:linear-gradient(120deg,#eef0f2 0%,#e3e8ee 50%,#dfe6ec 100%)"></span>
  <div class="abs copy">
    <div class="eyebrow">Locations</div>
    <h2 class="h2">Professional, Creative, Flexible,<br>Scalable Workspace</h2>
    <p class="body">Lorem Ipsum is simply dummy text of the printing and typesetting industry.<br>Lorem Ipsum has been the industry's standard dummy text.</p>
  </div>
  <div class="abs loc-card" style="left:572px">
    <span class="ph" role="img" aria-label="Bright atrium interior with columns" style="position:relative;height:200px;background:linear-gradient(180deg,#6f6a63 0%,#c9c1b2 60%,#8a8070 100%)"></span>
    <div class="txt"><h4>Los Angeles</h4><p>3 buildings across this location.</p><span class="btn">Explore this</span></div>
  </div>
  <div class="abs loc-card" style="left:901px">
    <span class="ph" role="img" aria-label="Interior atrium with balconies and railings" style="position:relative;height:200px;background:linear-gradient(180deg,#3f3a35 0%,#b8b2a8 60%,#7d766a 100%)"></span>
    <div class="txt"><h4>Chicago</h4><p>3 buildings across this location.</p><span class="btn">Explore this</span></div>
  </div>
  <div class="abs dots" style="left:840px;top:692px"><span class="on"></span><span></span><span></span><span></span></div>
</section>

<section class="listings">
  <div class="eyebrow">Listing</div>
  <div class="abs bar"></div>
  <h2 class="h2">Browse Listings in These Areas</h2>
  <p class="body">Lorem Ipsum is simply dummy text of the printing and typesetting industry.<br>Lorem Ipsum has been the industry's standard dummy text.</p>

  <div class="abs tile" style="left:90px;top:287px;width:667px;height:225px" role="img" aria-label="Large office building exterior">
    <span class="ph" style="inset:0;background:linear-gradient(180deg,#8aa3c8 0%,#6c6a66 60%,#4c4a46 100%)"></span>
    <div class="inner"><h5>LOS ANGELES</h5><p>The family areas</p><span class="tag">12 LISTING</span></div>
  </div>
  <div class="abs tile" style="left:770px;top:287px;width:326px;height:217px" role="img" aria-label="Atrium with staircase railings">
    <span class="ph" style="inset:0;background:linear-gradient(180deg,#4a4540 0%,#9a938a 55%,#c8c0b2 100%)"></span>
    <div class="inner"><h5>CHICAGO</h5><p>The family areas</p><span class="tag">15 LISTING</span></div>
  </div>
  <div class="abs tile" style="left:90px;top:525px;width:241px;height:161px" role="img" aria-label="Empty retail space with wooden floor">
    <span class="ph" style="inset:0;background:linear-gradient(135deg,#c9a06c 0%,#8a6a48 60%,#5e4a38 100%)"></span>
    <div class="inner"><h5>SAN JOSE</h5><p>The family areas</p><span class="tag">17 LISTING</span></div>
  </div>
  <div class="abs tile" style="left:345px;top:525px;width:496px;height:239px" role="img" aria-label="Shopping center exterior with parking and bare trees">
    <span class="ph" style="inset:0;background:linear-gradient(180deg,#5f82c0 0%,#8b8a86 60%,#5a5a5a 100%)"></span>
    <div class="inner"><h5>COLUMBUS</h5><p>The family areas</p><span class="tag">20 LISTING</span></div>
  </div>
  <div class="abs tile" style="left:855px;top:525px;width:241px;height:161px" role="img" aria-label="Atrium interior with balconies">
    <span class="ph" style="inset:0;background:linear-gradient(180deg,#5e5852 0%,#a9a297 60%,#7a7266 100%)"></span>
    <div class="inner"><h5>SAN FRANCISCO</h5><p>The family areas</p><span class="tag">22 LISTING</span></div>
  </div>
</section>

<section class="why">
  <span class="ph" role="img" aria-label="Building with steeple roof, trees and parked cars" style="left:0;top:0;width:502px;height:682px;background:linear-gradient(170deg,#3a68c4 0%,#bcc6d4 40%,#7f8c6a 75%,#585e62 100%)"></span>
  <div class="abs copy">
    <div class="eyebrow">Your Benefits</div>
    <h2 class="h2">Why Choose Us</h2>
    <p class="body">Lorem Ipsum is simply dummy text of the printing and typesetting industry.<br>Lorem Ipsum has been the industry's standard dummy text.</p>
  </div>
  <div class="abs benefit" style="left:566px;top:286px"><span class="icon-circle"><svg width="16" height="16" viewBox="0 0 16 16" fill="#fff"><rect x="3" y="2" width="10" height="13"/></svg></span><div><h4>Workspace</h4><p>Lorem ipsum dolor sit amet, consectetur adipiscing elit.</p></div></div>
  <div class="abs benefit" style="left:853px;top:286px"><span class="icon-circle soft"><svg width="16" height="16" viewBox="0 0 16 16" fill="var(--orange)"><circle cx="8" cy="8" r="4"/></svg></span><div><h4>Technology</h4><p>Lorem ipsum dolor sit amet, consectetur adipiscing elit.</p></div></div>
  <div class="abs benefit" style="left:566px;top:384px"><span class="icon-circle soft"><svg width="16" height="16" viewBox="0 0 16 16" fill="none" stroke="var(--orange)" stroke-width="2"><rect x="3" y="2" width="10" height="12"/></svg></span><div><h4>Facilities</h4><p>Lorem ipsum dolor sit amet, consectetur adipiscing elit.</p></div></div>
  <div class="abs benefit" style="left:853px;top:384px"><span class="icon-circle soft"><svg width="16" height="16" viewBox="0 0 16 16" fill="var(--orange)"><rect x="2" y="6" width="5" height="9"/><rect x="9" y="2" width="5" height="13"/></svg></span><div><h4>Global network</h4><p>Lorem ipsum dolor sit amet, consectetur adipiscing elit.</p></div></div>
  <div class="abs benefit" style="left:566px;top:481px"><span class="icon-circle soft"><svg width="16" height="16" viewBox="0 0 16 16" fill="none" stroke="var(--orange)" stroke-width="2"><circle cx="8" cy="5" r="3"/><path d="M2 15c0-4 3-6 6-6s6 2 6 6"/></svg></span><div><h4>Professional</h4><p>Lorem ipsum dolor sit amet, consectetur adipiscing elit.</p></div></div>
  <div class="abs benefit" style="left:853px;top:481px"><span class="icon-circle soft"><svg width="16" height="16" viewBox="0 0 16 16" fill="none" stroke="var(--orange)" stroke-width="2"><rect x="2" y="5" width="12" height="9"/><path d="M6 5V2h4v3"/></svg></span><div><h4>Benefits</h4><p>Lorem ipsum dolor sit amet, consectetur adipiscing elit.</p></div></div>
</section>

<section class="cta">
  <p>Would you like to Build your Dream Shop with Us? <b>Enquire Here</b> &nbsp;&#8250;</p>
</section>

<section class="contact-sec">
  <div class="eyebrow">Contact Us</div>
  <h2 class="h2">Get Some Enquiry</h2>
  <p class="body">Lorem Ipsum is simply dummy text of the printing and typesetting industry.<br>Lorem Ipsum has been the industry's standard dummy text.</p>
  <div class="abs cbox" style="left:88px"><svg width="16" height="12" viewBox="0 0 16 12" fill="#fff"><path d="M0 0h16v12H0z"/><path d="M0 0l8 6 8-6" stroke="#1f3673" fill="none" stroke-width="1.5"/></svg>Contact Us</div>
  <div class="abs cbox" style="left:261px"><svg width="14" height="14" viewBox="0 0 14 14" fill="#fff"><circle cx="7" cy="4" r="3.5"/><path d="M0 14c0-4 3-6 7-6s7 2 7 6z"/></svg>Apply online</div>
  <div class="abs cbox" style="left:434px"><svg width="14" height="14" viewBox="0 0 24 24" fill="#fff"><path d="M6.6 10.8a15 15 0 006.6 6.6l2.2-2.2a1 1 0 011-.3 11 11 0 003.6.6 1 1 0 011 1V20a1 1 0 01-1 1A17 17 0 013 4a1 1 0 011-1h3.5a1 1 0 011 1 11 11 0 00.6 3.6 1 1 0 01-.3 1z"/></svg>0129-55210</div>
  <span class="ph" role="img" aria-label="Close-up of colourful app and social media keyboard keys" style="left:614px;top:296px;width:482px;height:316px;background:linear-gradient(135deg,#1b3a9c 0%,#3f7ce0 45%,#9fc7f2 100%)"></span>
  <div class="abs quote">
    "Lorem Ipsum is simply dummy text of the printing and typesetting industry. Lorem Ipsum has been the industry's standard dummy text ever since"
    <div class="qd"><span class="on"></span><span></span><span></span></div>
  </div>
</section>

</body>
</html>
```